Flyer for Makeup Class

A flyer for my makeup class promotion. I am a make up artist starting a group class to teach makeup to ladies. I have attached some verbiage handwritten. My picture is the one in pink hijab. I have also attached some inspiration ideas and color combination (the colors in the cake design are the ones I want to use).

Target Market(s)

Ladies looking to learn make up from a make up artist

Industry/Entity Type

Hair And Beauty

Requirements
Must have
• The verbiage / description that I have hand written should be written using graphics and nice fonts. You can change the exact wording to make it better.

```html
<!DOCTYPE html>
<html lang="en">
<head>
<meta charset="utf-8">
<title>Makeup Class Flyer</title>
<link href="https://fonts.googleapis.com/css2?family=Playfair+Display:wght@700&family=Montserrat:wght@600;700;800&family=Lora:wght@400&family=Dancing+Script:wght@600&display=swap" rel="stylesheet">
<style>
  :root {
    --bg: #ecebe8;
    --paper: #ffffff;
    --pink: #f7b9c6;
    --pink-soft: #fbd7de;
    --pink-pale: #fce6ea;
    --pink-deep: #e8718d;
    --gold: #f4b63f;
    --gold-pale: #fbe6bd;
    --ink: #1e1e1e;
    --text: #3a3a3a;
  }
  * { box-sizing: border-box; margin: 0; padding: 0; }
  html, body { width: 1200px; height: 798px; overflow: hidden; background: var(--bg); }
  .flyer {
    position: absolute; left: 365px; top: 29px;
    width: 470px; height: 740px;
    background: var(--paper);
    box-shadow: 0 4px 18px rgba(0,0,0,.12);
  }
  .frame {
    position: absolute; left: 34px; top: 70px; width: 402px; height: 600px;
    border: 3px solid var(--pink);
  }
  .art-lipstick {
    position: absolute; left: 22px; top: 32px; width: 78px; height: 104px;
    background: var(--pink-pale);
  }
  .art-tools {
    position: absolute; left: 372px; top: 44px; width: 58px; height: 80px;
    background: var(--gold-pale);
  }
  .banner {
    position: absolute; left: 62px; top: 106px; width: 318px; height: 34px;
    background: var(--pink);
    font: 800 12.5px/34px "Montserrat", sans-serif;
    letter-spacing: .6px; text-align: center; color: var(--ink);
  }
  .name {
    position: absolute; left: 62px; top: 160px;
    font: 700 44px/1 "Playfair Display", serif; color: var(--ink); letter-spacing: .5px;
    white-space: nowrap;
  }
  .role {
    position: absolute; left: 66px; top: 212px;
    font: 600 17px/1 "Dancing Script", cursive; color: var(--gold);
  }
  .rule { position: absolute; left: 62px; top: 238px; width: 350px; height: 2px; background: var(--gold); }
  .summary {
    position: absolute; left: 66px; top: 264px; width: 146px;
    font: 400 13px/1.55 "Lora", serif; color: var(--text);
  }
  .portrait {
    position: absolute; left: 218px; top: 250px; width: 222px; height: 420px;
    background: linear-gradient(180deg, #f6e9ea 0%, #f2c6cf 55%, #f0a8b8 100%);
  }
  .details {
    position: absolute; left: 34px; top: 458px; width: 234px; height: 108px;
    background: var(--pink-soft); display: flex;
  }
  .details .col { flex: 1; padding: 12px 8px 0 18px; }
  .details .col + .col { border-left: 2px solid var(--pink); padding-left: 12px; }
  .label { font: 800 17px/1 "Montserrat", sans-serif; color: var(--ink); margin-bottom: 10px; }
  .value { font: 600 8.5px/1.55 "Montserrat", sans-serif; color: var(--text); text-transform: uppercase; white-space: nowrap; }
  .contact {
    position: absolute; left: 48px; top: 584px; width: 168px;
    font: 700 8.5px/1.8 "Montserrat", sans-serif; color: var(--pink-deep); text-transform: uppercase;
  }
  .contact .handle { text-transform: none; }
</style>
</head>
<body>
  <main class="flyer">
    <div class="frame"></div>
    <div class="art-lipstick" role="img" aria-label="Illustration of a lipstick"></div>
    <div class="art-tools" role="img" aria-label="Illustration of makeup brushes"></div>
    <div class="banner">EXCLUSIVE MAKE UP CLASSES BY</div>
    <h1 class="name">SAMIRA QADIR</h1>
    <p class="role">Makeup Artist</p>
    <div class="rule"></div>
    <p class="summary">This class is packed with loads of information tips, live demos, goodie bag, certificate, Q&amp;A, lunch &amp; much more...</p>
    <div class="portrait" role="img" aria-label="Photo of the makeup artist wearing a pink hijab"></div>
    <section class="details">
      <div class="col">
        <p class="label">VENUE</p>
        <p class="value">Palm Court Hall<br>Cedar Plaza<br>(Riverton)</p>
      </div>
      <div class="col">
        <p class="label">DATE</p>
        <p class="value">6th April 2019<br>11:00AM–3:00PM</p>
      </div>
    </section>
    <p class="contact">
      To book your place contact:<br>
      0300 555 0147<br>
      0321 555 0298<br>
      Instagram: <span class="handle">@samiraqadirstudio</span>
    </p>
  </main>
</body>
</html>
```